SkyvoraQ Business Cards and Stationary Design

Need a design for our business cards and stationary. I want to carry on the theme of the logo. I want the business cards to have a design on the back. I would like the business cards and the stationary to carry the same theme, design scheme, and branding

Target Market(s)

Airlines and Maintenance Facilities

Industry/Entity Type

Aviation

Contact Information for Business Card

Name
Position Title
Address: 4827 Tollbeck Lane, Fort Pierce, Florida, 34951
Office Number
Mobile Number
Email
Website

Font styles to use
Serif
Sans Serif

Colors

Designer to choose colors to be used in the design.

```html
<!DOCTYPE html>
<html lang="en">
<head>
<meta charset="utf-8">
<title>SkyvoraQ Business Cards</title>
<link rel="stylesheet" href="https://fonts.googleapis.com/css2?family=Montserrat:wght@500;700;800&display=swap">
<style>
  :root {
    --backdrop: #eceeed;
    --navy: #0b2a4f;
    --sky: #1ea0e6;
    --deep-blue: #0a4a9a;
    --white: #ffffff;
    --ink: #0b2a4f;
    --ink-light: #dfe8f3;
  }
  * { margin: 0; padding: 0; box-sizing: border-box; }
  html, body { width: 1200px; height: 900px; overflow: hidden; }
  body {
    background: var(--backdrop);
    font-family: "Montserrat", Arial, sans-serif;
    position: relative;
  }
  .card {
    position: absolute;
    width: 514px;
    height: 298px;
    border-radius: 24px;
    overflow: hidden;
    box-shadow: 0 2px 6px rgba(0,0,0,0.12);
  }
  .card--dark { background: var(--navy); color: var(--ink-light); }
  .card--light { background: var(--white); color: var(--ink); }
  .card--front-dark { left: 73px; top: 137px; }
  .card--back-light { left: 615px; top: 137px; }
  .card--front-light { left: 73px; top: 463px; }
  .card--back-dark { left: 615px; top: 463px; }

  .brand {
    position: absolute;
    left: 0; right: 0; top: 76px;
    display: flex; flex-direction: column; align-items: center;
    gap: 26px;
  }
  .brand__dot {
    width: 76px; height: 76px; border-radius: 50%;
    background: var(--sky);
  }
  .brand__name {
    font-weight: 800;
    font-size: 32px;
    line-height: 36px;
    letter-spacing: 6px;
    margin-right: -6px;
  }
  .card--dark .brand__name { color: var(--white); }
  .card--light .brand__name { color: var(--navy); }

  .ring { position: absolute; left: 0; top: 0; }

  .marker {
    position: absolute; left: 0; top: 84px;
    width: 0; height: 0;
    border-top: 8px solid transparent;
    border-bottom: 8px solid transparent;
    border-left: 14px solid var(--sky);
  }
  .contact { position: absolute; left: 41px; top: 80px; }
  .contact__name { font-size: 13px; font-weight: 700; color: var(--sky); line-height: 16px; }
  .contact__role { font-size: 9px; font-weight: 700; line-height: 12px; letter-spacing: 0.2px; }
  .card--dark .contact__role { color: var(--white); }
  .contact__list { list-style: none; margin-top: 10px; }
  .contact__item {
    display: flex; align-items: center; gap: 6px;
    font-size: 11px; font-weight: 500; line-height: 14.5px;
  }
  .contact__icon {
    width: 10px; height: 10px; border-radius: 50%;
    background: var(--sky); flex: none;
    position: relative;
  }
  .contact__icon::after {
    content: ""; position: absolute; left: 3px; top: 3px;
    width: 4px; height: 4px; border-radius: 1px; background: var(--white);
  }
  .contact__company { margin-top: 9px; font-size: 11px; font-weight: 800; letter-spacing: 2.5px; line-height: 14px; }
  .contact__address { font-size: 11px; font-weight: 500; line-height: 14.5px; }
  .card--back-dark .contact__address { margin-top: 9px; }

  .back-name {
    position: absolute; left: 277px; top: 138px; width: 200px;
    text-align: center;
    font-size: 14px; font-weight: 800; letter-spacing: 3px; color: var(--white);
  }
</style>
</head>
<body>

  <section class="card card--dark card--front-dark" aria-label="Card front, dark">
    <div class="brand">
      <span class="brand__dot"></span>
      <span class="brand__name">SKYVORAQ</span>
    </div>
  </section>

  <section class="card card--light card--back-light" aria-label="Card back, light">
    <svg class="ring" width="514" height="298" viewBox="0 0 514 298" aria-hidden="true">
      <defs>
        <linearGradient id="ringLight" x1="0" y1="0" x2="1" y2="1">
          <stop offset="0" stop-color="#1ea0e6"/>
          <stop offset="1" stop-color="#0a4a9a"/>
        </linearGradient>
      </defs>
      <circle cx="378" cy="150" r="140" fill="none" stroke="url(#ringLight)" stroke-width="18"/>
    </svg>
    <span class="marker"></span>
    <div class="contact">
      <p class="contact__name">MARCUS HELLAND</p>
      <p class="contact__role">MANAGING DIRECTOR</p>
      <ul class="contact__list">
        <li class="contact__item"><span class="contact__icon"></span>5550 214 773</li>
        <li class="contact__item"><span class="contact__icon"></span>5550 389 416</li>
        <li class="contact__item"><span class="contact__icon"></span>m.helland@skyvoraq.com</li>
        <li class="contact__item"><span class="contact__icon"></span>www.skyvoraq.com</li>
      </ul>
      <p class="contact__company">SKYVORAQ</p>
      <p class="contact__address">4827 Tollbeck Lane<br>Fort Pierce, Florida, 34951</p>
    </div>
  </section>

  <section class="card card--light card--front-light" aria-label="Card front, light">
    <div class="brand">
      <span class="brand__dot"></span>
      <span class="brand__name">SKYVORAQ</span>
    </div>
  </section>

  <section class="card card--dark card--back-dark" aria-label="Card back, dark">
    <svg class="ring" width="514" height="298" viewBox="0 0 514 298" aria-hidden="true">
      <defs>
        <linearGradient id="ringDark" x1="0" y1="0" x2="1" y2="1">
          <stop offset="0" stop-color="#1ea0e6"/>
          <stop offset="1" stop-color="#0a4a9a"/>
        </linearGradient>
      </defs>
      <circle cx="378" cy="150" r="140" fill="none" stroke="url(#ringDark)" stroke-width="18"/>
    </svg>
    <span class="marker"></span>
    <div class="contact">
      <p class="contact__name">MARCUS HELLAND</p>
      <p class="contact__role">MANAGING DIRECTOR</p>
      <ul class="contact__list">
        <li class="contact__item"><span class="contact__icon"></span>5550 214 773</li>
        <li class="contact__item"><span class="contact__icon"></span>5550 389 416</li>
        <li class="contact__item"><span class="contact__icon"></span>m.helland@skyvoraq.com</li>
        <li class="contact__item"><span class="contact__icon"></span>www.skyvoraq.com</li>
      </ul>
      <p class="contact__address">4827 Tollbeck Lane<br>Fort Pierce, Florida, 34951</p>
    </div>
    <p class="back-name">SKYVORAQ</p>
  </section>

</body>
</html>
```